Business Card Design For A Renovation Contractor Company

We need a business card for a new company based in Singapore, our company name is "KT Planora". We are a renovation contractor that builds designs into reality. We build more of F&B restaurants, retail stores and commercial offices. We work very closely with designers. The final design should communicate to our client that we are a company that you can trust, that will plan and complete your project without giving you a headache. I like my client to remember my company as "KT". The beauty of SIMPLE is important.

Industry/Entity Type

Contractor

Requirements
Nice to have
• Black or Red base

```html
<!DOCTYPE html>
<html lang="en">
<head>
<meta charset="utf-8">
<title>KT Planora – Business Card</title>
<link rel="stylesheet" href="https://fonts.googleapis.com/css2?family=Open+Sans:wght@400&display=swap">
<style>
  :root {
    --card-red: #bf0000;
    --card-black: #0a0a0a;
    --card-white: #f7f7f3;
    --ink-dark: #111111;
    --ink-light: #ffffff;
    --brand-font: "Open Sans", Arial, sans-serif;
  }
  html, body {
    margin: 0;
    padding: 0;
    width: 1200px;
    height: 687px;
    overflow: hidden;
    background: var(--card-red);
  }
  .business-card {
    position: relative;
    width: 1200px;
    height: 687px;
    overflow: hidden;
    font-family: var(--brand-font);
  }
  .card-shapes {
    position: absolute;
    inset: 0;
    display: block;
  }
  .shape-red { fill: var(--card-red); }
  .shape-white { fill: var(--card-white); }
  .shape-black { fill: var(--card-black); }
  .brand-dot { fill: var(--card-red); }
  .brand-rule { stroke: var(--ink-dark); stroke-width: 1.5; }

  .brand-name {
    position: absolute;
    left: 25px;
    top: 160px;
    margin: 0;
    font-size: 62px;
    font-weight: 400;
    line-height: 1;
    letter-spacing: 1px;
    color: var(--ink-dark);
    white-space: nowrap;
  }
  .brand-tagline {
    position: absolute;
    left: 40px;
    top: 231px;
    margin: 0;
    font-size: 22px;
    font-weight: 400;
    line-height: 1;
    letter-spacing: 2.2px;
    color: var(--ink-dark);
    white-space: nowrap;
  }
  .contact-details {
    position: absolute;
    left: 618px;
    top: 274px;
    margin: 0;
    font-style: normal;
    font-size: 33px;
    line-height: 41px;
    color: var(--ink-light);
    white-space: nowrap;
  }
</style>
</head>
<body>
  <main class="business-card">
    <svg class="card-shapes" viewBox="0 0 1200 687" width="1200" height="687" aria-hidden="true">
      <rect class="shape-red" x="0" y="0" width="1200" height="687"/>
      <circle class="shape-white" cx="218" cy="80" r="290"/>
      <circle class="shape-white" cx="967" cy="379" r="438"/>
      <circle class="shape-black" cx="990" cy="379" r="441"/>
      <circle class="brand-dot" cx="207" cy="86" r="58"/>
      <line class="brand-rule" x1="25" y1="229" x2="400" y2="229"/>
    </svg>

    <h1 class="brand-name">KT Planora</h1>
    <p class="brand-tagline">from plan to finished space</p>

    <address class="contact-details">
      Email: kevin@ktplanora.com<br>
      Address: 18 Marlow Lane<br>
      #07-2203 Marlow Business Hub<br>
      Singapore 430118
    </address>
  </main>
</body>
</html>
```